Direct Response Landing Page for Paid Search Campaigns for TrailKeepers.com

TrailKeepers.com is a leading people search / public records company, providing consumers with instant, accurate access to public records. We are a direct response org focused on engaging the user and converting the user to a customer. Our product returns instant search results based on a name or phone search. We are looking for a landing page to test out, against our current "Home Page." We will drive traffic to this page via paid search terms (ie., "people search, find people"). We would like a landing page with a headline, search forms, CTA Search button, with features/beneifts about the service and company. Specific Key Messaging will be provided.

Target Market(s)

Consumers. Skew slightly female, ages 40+

Industry/Entity Type

It Company

Number of Pages Required

1 page

Font styles to use
Sans Serif

Requirements
Must have
• Use of Logo; upper left corner, consistent w/ TrailKeepers.com.
• Use of two HTML search forms (prefer a toggle between the two). Users must type in a search query in a search form for either:
• 1. First Name, Last Name, City, State
• 2. Phone # (area code w/ phone #)
• Call to Action: "Search" button
Should not have
• Should not include TrailKeepers.com's standard nav at the top.

```html
<!DOCTYPE html>
<html lang="en">
<head>
<meta charset="utf-8">
<title>TrailKeepers.com – People Search</title>
<link rel="stylesheet" href="https://fonts.googleapis.com/css2?family=Questrial&family=Nunito:wght@800&family=Arimo:wght@400;700&display=swap">
<style>
:root{
  --blue:#2b86c8;
  --blue-panel:#3a8ccf;
  --navy:#02426f;
  --tab-dark:#4a4e52;
  --green:#13913c;
  --grey-panel:#ececec;
  --text-dark:#3a3d40;
  --text-soft:#4a4d50;
  --footer-soft:#e3f0f9;
  --field-soft:#d5e6f2;
  --white:#ffffff;
}
*{box-sizing:border-box;margin:0;padding:0}
html,body{width:1198px;height:1200px;overflow:hidden;background:var(--white)}
body{position:relative;font-family:'Arimo',Arial,sans-serif;color:var(--text-dark)}

.page-header{position:absolute;left:0;top:0;width:1198px;height:100px}
.brand{position:absolute;left:100px;top:34px;display:flex;align-items:center;gap:10px}
.brand-mark{width:14px;height:14px;background:var(--blue)}
.brand-name{font-family:'Questrial',sans-serif;font-size:30px;color:var(--blue);line-height:1}
.headline{position:absolute;right:97px;top:51px;font-family:'Questrial',sans-serif;font-size:25px;color:var(--blue);letter-spacing:.3px;white-space:nowrap}

.hero{position:absolute;left:0;top:100px;width:1198px;height:492px}
.hero-photo{position:absolute;inset:0;background:linear-gradient(180deg,#7ea6c4 0%,#c9c6b8 45%,#e8b784 62%,#5a4a3e 78%,#2a2622 100%)}
.search-card{position:absolute;left:569px;top:54px;width:531px}
.tabs{display:flex;height:41px}
.tab{font-family:'Questrial',sans-serif;font-size:18px;color:var(--white);display:flex;align-items:center;justify-content:center;letter-spacing:.2px}
.tab.active{background:var(--blue-panel);width:211px}
.tab.inactive{background:var(--tab-dark);width:207px}
.search-form{position:relative;background:var(--blue-panel);height:187px}
.field{position:absolute;width:246px;height:36px;background:var(--white);font:14px 'Arimo',sans-serif;color:var(--blue);padding-left:13px;display:flex;align-items:center}
.search-btn{position:absolute;left:16px;top:123px;width:502px;height:46px;background:var(--navy);color:var(--white);font:700 17px 'Arimo',sans-serif;display:flex;align-items:center;justify-content:center;letter-spacing:.3px}
.about{background:var(--grey-panel);height:147px;padding:19px 30px}
.about h2{font-family:'Questrial',sans-serif;font-weight:400;font-size:24px;color:var(--text-soft);margin-bottom:10px;letter-spacing:-.2px}
.about ul{list-style:none;font-family:'Questrial',sans-serif;font-size:14px;letter-spacing:.95px;color:var(--text-soft)}
.about li{position:relative;padding-left:16px;line-height:19.5px;white-space:nowrap}
.about li::before{content:"•";position:absolute;left:-3px;font-size:10px}

.feature-icon{position:absolute;display:block}
.feature-title{position:absolute;width:340px;text-align:center;font-family:'Nunito',sans-serif;font-weight:800;font-size:24px;line-height:30px;color:var(--blue)}
.feature-text{position:absolute;text-align:center;font-size:14px;line-height:17px;color:var(--text-dark)}
.learn{position:absolute;top:874px;width:153px;height:36px;background:var(--green);color:var(--white);font:800 13px 'Nunito',sans-serif;display:flex;align-items:center;padding-left:37px;text-decoration:none}
.learn::before{content:"";position:absolute;left:10px;top:14px;border-left:5px solid var(--white);border-top:4px solid transparent;border-bottom:4px solid transparent}

.site-footer{position:absolute;left:0;top:1028px;width:1198px;height:172px;background:var(--blue)}
.footer-brand{position:absolute;left:102px;top:56px;display:flex;align-items:center;gap:10px}
.footer-brand .brand-mark{background:var(--white)}
.footer-brand .brand-name{color:var(--white)}
.follow{position:absolute;left:524px;top:38px}
.follow h4,.newsletter h4{font-family:'Questrial',sans-serif;font-weight:400;font-size:18px;color:var(--white)}
.socials{display:flex;gap:10px;margin-top:22px}
.social{width:28px;height:28px;border-radius:3px;background:var(--navy)}
.newsletter{position:absolute;left:781px;top:40px}
.newsletter p{font-size:11px;color:var(--footer-soft);margin-top:4px;white-space:nowrap}
.signup{display:flex;gap:4px;margin-top:8px}
.email{width:233px;height:27px;background:var(--field-soft);font-size:11px;color:var(--blue);padding-left:9px;display:flex;align-items:center}
.subscribe{width:83px;height:27px;background:var(--navy);color:var(--white);font-size:11px;display:flex;align-items:center;justify-content:center}
</style>
</head>
<body>
<header class="page-header">
  <div class="brand"><span class="brand-mark"></span><span class="brand-name">TrailKeepers.com</span></div>
  <p class="headline">Since 1999, Your Trusted Online People Search Source</p>
</header>

<section class="hero">
  <div class="hero-photo" role="img" aria-label="Silhouettes of business people standing by tall windows at sunset, long shadows on the floor"></div>
  <div class="search-card">
    <div class="tabs"><div class="tab active">Search By Name</div><div class="tab inactive">Search By Phone</div></div>
    <form class="search-form">
      <div class="field" style="left:16px;top:29px">First Name</div>
      <div class="field" style="left:271px;top:29px">Last Name</div>
      <div class="field" style="left:16px;top:73px">City</div>
      <div class="field" style="left:271px;top:73px">State</div>
      <div class="search-btn">SEARCH</div>
    </form>
    <div class="about">
      <h2>WHO WE ARE</h2>
      <ul>
        <li>Launched online in 1999</li>
        <li>Leading Data-as-a-Service Public Records Organization</li>
        <li>Privacy and Security are paramount to our Organization</li>
      </ul>
    </div>
  </div>
</section>

<section class="features">
  <svg class="feature-icon" style="left:228px;top:675px" width="52" height="66" viewBox="0 0 52 66"><circle cx="26" cy="18" r="15" fill="none" stroke="#2b86c8" stroke-width="4"/><path d="M26 9v9l6 4" stroke="#2b86c8" stroke-width="3" fill="none"/><path d="M2 66v-10a9 9 0 0 1 9-9h30a9 9 0 0 1 9 9v10z" fill="#2b86c8"/></svg>
  <h3 class="feature-title" style="left:83px;top:760px">Save Time</h3>
  <p class="feature-text" style="left:123px;top:797px;width:270px">TrailKeepers has people, phone, background, property and criminal, at your fingertips.</p>

  <svg class="feature-icon" style="left:576px;top:667px" width="70" height="70" viewBox="0 0 70 70"><rect x="40" y="0" width="30" height="30" fill="#2b86c8"/><text x="55" y="23" font-family="Arimo" font-weight="700" font-size="22" fill="#fff" text-anchor="middle">$</text><path d="M2 70v-12a9 9 0 0 1 9-9h26a9 9 0 0 1 9 9v12z" fill="#2b86c8"/><circle cx="24" cy="30" r="12" fill="#2b86c8"/></svg>
  <h3 class="feature-title" style="left:429px;top:756px">Save $</h3>
  <p class="feature-text" style="left:466px;top:797px;width:270px">We do the vetting for you to access local, state and nationwide records =&nbsp; delivering you AFFORDABLE UNLIMITED access.</p>

  <svg class="feature-icon" style="left:914px;top:690px" width="74" height="50" viewBox="0 0 74 50"><g fill="#2b86c8"><circle cx="6" cy="15" r="5"/><rect x="0" y="22" width="12" height="18"/><circle cx="68" cy="15" r="5"/><rect x="62" y="22" width="12" height="18"/><circle cx="21" cy="10" r="6"/><rect x="14" y="18" width="15" height="24"/><circle cx="53" cy="10" r="6"/><rect x="45" y="18" width="15" height="24"/><circle cx="37" cy="7" r="7"/><rect x="28" y="16" width="18" height="34"/></g></svg>
  <h3 class="feature-title" style="left:781px;top:759px">Comprehensive</h3>
  <p class="feature-text" style="left:816px;top:797px;width:270px">We Provide Instant Access to Billions of People Search &amp; Background Records</p>
</section>
<a class="learn" style="left:175px">LEARN MORE</a>
<a class="learn" style="left:528px">LEARN MORE</a>
<a class="learn" style="left:881px">LEARN MORE</a>

<footer class="site-footer">
  <div class="footer-brand"><span class="brand-mark"></span><span class="brand-name">TrailKeepers.com</span></div>
  <div class="follow">
    <h4>Follow Us</h4>
    <div class="socials"><span class="social" aria-label="Social link one"></span><span class="social" aria-label="Social link two"></span><span class="social" aria-label="Social link three"></span></div>
  </div>
  <div class="newsletter">
    <h4>Newsletter</h4>
    <p>Subscribe to recieve inspiration, ideas, and news in your inbox.</p>
    <div class="signup"><div class="email">Email Address</div><div class="subscribe">Subscribe</div></div>
  </div>
</footer>
</body>
</html>
```